Business Card Design

We need a business card designed for our new company. Prefer a black card with white logo & writing.

Contact Information for Business Card

Dale Pickett, address: 7-4417 Larchmere Avenue, Abbotsford, BC, V3K 2R9, Office Phone: 604-555-0172, Cell: 604-555-0138, Email: dale@kelsoncoatworks.ca

Colors

Designer to choose only greyscale colors for use in the design.

```html
<!DOCTYPE html>
<html lang="en">
<head>
<meta charset="utf-8">
<title>Kelson Coatworks Business Card</title>
<link href="https://fonts.googleapis.com/css2?family=Poppins:wght@400;600;700&display=swap" rel="stylesheet">
<style>
  :root {
    --ink: #1c1a1a;
    --paper: #ffffff;
    --stripe: #7a7b7d;
    --rule: #c9c9c9;
    --backdrop: #e6e6e6;
  }
  * { margin: 0; padding: 0; box-sizing: border-box; }
  html, body { width: 1200px; height: 900px; overflow: hidden; }
  body {
    background: var(--backdrop);
    font-family: "Poppins", sans-serif;
    display: flex;
    flex-direction: column;
    align-items: center;
    justify-content: center;
    gap: 40px;
  }
  .card {
    width: 700px;
    height: 400px;
    position: relative;
    overflow: hidden;
    box-shadow: 0 6px 18px rgba(0,0,0,0.18);
  }
  .card-front {
    background: var(--ink);
    display: flex;
    align-items: center;
    justify-content: center;
  }
  .brand {
    display: flex;
    align-items: center;
    gap: 16px;
    font-weight: 700;
    text-transform: uppercase;
    letter-spacing: 1px;
  }
  .brand-dot {
    width: 22px; height: 22px; border-radius: 50%;
  }
  .card-front .brand { color: var(--paper); font-size: 52px; }
  .card-front .brand-dot { background: var(--paper); }
  .card-back { background: var(--paper); }
  .wave { position: absolute; inset: 0; width: 100%; height: 100%; }
  .wave-stripe { fill: var(--stripe); }
  .wave-band { fill: var(--ink); }
  .contact {
    position: absolute;
    left: 60px;
    top: 60px;
    color: var(--ink);
  }
  .contact-name {
    font-size: 26px;
    font-weight: 700;
    text-transform: uppercase;
    letter-spacing: 0.5px;
  }
  .rule {
    width: 46px; height: 1px; background: var(--rule);
    margin: 14px 0 12px;
  }
  .contact-lines { list-style: none; font-size: 17px; line-height: 1.55; }
  .contact-lines li { display: flex; align-items: center; gap: 10px; }
  .icon { width: 16px; height: 16px; fill: none; stroke: var(--ink); stroke-width: 1.8; }
  .address { font-size: 17px; line-height: 1.4; }
  .card-back .brand {
    position: absolute;
    right: 48px;
    top: 78px;
    color: var(--ink);
    font-size: 34px;
    gap: 12px;
  }
  .card-back .brand-dot { background: var(--ink); width: 16px; height: 16px; }
</style>
</head>
<body>
  <section class="card card-front">
    <div class="brand"><span class="brand-dot"></span>Kelson Coatworks</div>
  </section>

  <section class="card card-back">
    <svg class="wave" viewBox="0 0 700 400" preserveAspectRatio="none" aria-hidden="true">
      <path class="wave-stripe" d="M0,322 C210,322 390,272 560,165 C390,292 210,346 0,346 Z"/>
      <path class="wave-band" d="M0,400 L0,344 C210,344 390,292 540,190 C610,145 660,118 700,110 L700,400 Z"/>
    </svg>

    <div class="contact">
      <h1 class="contact-name">Dale Pickett</h1>
      <div class="rule"></div>
      <ul class="contact-lines">
        <li>
          <svg class="icon" viewBox="0 0 16 16"><path d="M3 2 L6 2 L7 5 L5 6.5 C6 9 7 10 9.5 11 L11 9 L14 10 L14 13 C8 14 2 8 3 2 Z"/></svg>
          604-555-0172
        </li>
        <li>
          <svg class="icon" viewBox="0 0 16 16"><rect x="4" y="1.5" width="8" height="13" rx="1.5"/><line x1="7" y1="12" x2="9" y2="12"/></svg>
          604-555-0138
        </li>
        <li>
          <svg class="icon" viewBox="0 0 16 16"><rect x="1.5" y="3.5" width="13" height="9"/><polyline points="1.5,3.5 8,9 14.5,3.5"/></svg>
          dale@kelsoncoatworks.ca
        </li>
      </ul>
      <div class="rule"></div>
      <p class="address">7-4417 Larchmere Avenue,<br>Abbotsford, BC, V3K 2R9</p>
    </div>

    <div class="brand"><span class="brand-dot"></span>Kelson Coatworks</div>
  </section>
</body>
</html>
```